Chicago Property Management Flyer

We need a brochure/flyer to market our property management services to Chicago property owners. I believe that my preference is single page, double sided, but a bi-fold or tri-fold format may also work. I have provided our logo, and some example images in case that is helpful. Refer to our website at http://www.lumevarpm.net/ for more info.

Industry/Entity Type

Property Management

Font styles to use
Sans Serif

```html
<!DOCTYPE html>
<html lang="en">
<head>
<meta charset="utf-8">
<title>Lumevar Property Management – Brochure</title>
<link rel="stylesheet" href="https://fonts.googleapis.com/css2?family=Crimson+Text:wght@400;600&display=swap">
<style>
  :root{
    --navy:#1f3f66;
    --contact:#3a78c0;
    --white:#ffffff;
    --page:#ffffff;
  }
  *{margin:0;padding:0;box-sizing:border-box}
  html,body{width:1200px;height:900px;overflow:hidden;background:var(--page)}
  body{position:relative;font-family:"Crimson Text",Georgia,serif}
  .brochure{position:absolute;left:22px;top:70px;width:1145px;height:760px;overflow:hidden;background:var(--white)}
  .brochure-art{position:absolute;inset:0;width:100%;height:100%}
  .brand{position:absolute;left:823px;top:104px;width:260px;text-align:center;color:var(--navy);font-weight:600;font-size:22px;letter-spacing:1.5px;line-height:1.05}
  .contact{position:absolute;left:62px;top:176px;color:var(--contact);font-size:16.5px;line-height:1.2}
  .contact p{margin-bottom:21px}
  .contact .indent{display:block;padding-left:98px}
  .contact .web{font-size:20px;letter-spacing:.3px}
  .building-photo{position:absolute;left:62px;top:392px;width:253px;height:168px;border-radius:10px;background:linear-gradient(160deg,#b9cfe2 0%,#d9cfae 40%,#a99b74 62%,#4f7a3a 85%,#3b6130 100%)}
  .tagline{position:absolute;color:var(--white);font-size:29px;letter-spacing:1px;white-space:nowrap}
  .tagline span{display:block}
  .tagline-left{left:478px;top:603px;line-height:34px}
  .tagline-left .l2{margin-top:6px}
  .tagline-left .l3{margin-top:-1px}
  .tagline-left .l4{margin-top:4px;margin-left:-3px}
  .tagline-right{left:795px;top:602px;line-height:28px}
</style>
</head>
<body>
<main class="brochure">
  <svg class="brochure-art" viewBox="0 0 1145 760" xmlns="http://www.w3.org/2000/svg">
    <defs>
      <linearGradient id="bandTop" x1="0" y1="0" x2="1" y2="1">
        <stop offset="0" stop-color="#1b6fb3"/><stop offset=".5" stop-color="#2f9ad8"/><stop offset="1" stop-color="#1b5e9c"/>
      </linearGradient>
      <linearGradient id="leftPanel" x1="0" y1="0" x2="0" y2="1">
        <stop offset="0" stop-color="#ffffff"/><stop offset=".28" stop-color="#d6e9f7"/><stop offset=".3" stop-color="#8dbfe3"/><stop offset=".6" stop-color="#74aedb"/><stop offset=".62" stop-color="#a8d0ee"/><stop offset="1" stop-color="#9ccaeb"/>
      </linearGradient>
      <linearGradient id="cityPhoto" x1="0" y1="0" x2="0" y2="1">
        <stop offset="0" stop-color="#dfe5ea"/><stop offset=".3" stop-color="#b4c2cc"/><stop offset=".5" stop-color="#5f6f7c"/><stop offset=".75" stop-color="#9b8574"/><stop offset="1" stop-color="#7f7a6e"/>
      </linearGradient>
      <linearGradient id="bottomBand" x1="0" y1="0" x2="1" y2="1">
        <stop offset="0" stop-color="#2d7fc0"/><stop offset=".5" stop-color="#1d5f94"/><stop offset="1" stop-color="#194f7e"/>
      </linearGradient>
    </defs>

    <rect class="left-panel" x="0" y="148" width="380" height="612" fill="url(#leftPanel)"/>

    <polygon class="top-band" points="0,0 755,0 382,148 0,148" fill="url(#bandTop)"/>

    <rect class="city-photo" role="img" aria-label="Photo of the Chicago skyline over city neighbourhoods" x="380" y="152" width="765" height="450" fill="url(#cityPhoto)"/>

    <polygon class="photo-band" points="380,152 380,222 820,400 1010,400" fill="#1b6e93" opacity=".62"/>
    <polygon class="photo-band" points="1145,145 1145,290 1000,410 870,410" fill="#1b6e93" opacity=".62"/>

    <path class="bottom-band" d="M0,700 C300,600 700,530 1145,512 L1145,760 L0,760 Z" fill="url(#bottomBand)"/>
    <path class="swoosh" d="M50,760 C380,610 760,545 1145,528" fill="none" stroke="#ffffff" stroke-width="5"/>
    <path class="swoosh-accent" d="M0,690 C320,585 720,522 1145,500" fill="none" stroke="#4aa3e0" stroke-width="6" opacity=".7"/>
  </svg>

  <div class="brand">LUMEVAR PROPERTY<br>MANAGEMENT</div>

  <div class="contact">
    <p>ADDRESS: 1870 S. Halvern Ave<span class="indent">Chicago IL 60616</span></p>
    <p>TEL: 773-555-0148</p>
    <p>EMAIL: miles@lumevarpm.net</p>
    <p class="web">www.lumevarpm.net</p>
  </div>

  <div class="building-photo" role="img" aria-label="Photo of a brick apartment building on a tree-lined street"></div>

  <p class="tagline tagline-left"><span class="l1">Managing CHV</span><span class="l2">Section 8 rentals</span><span class="l3">across Chicago</span><span class="l4">for over a decade</span></p>
  <p class="tagline tagline-right"><span>Leverage our</span><span>experience and expertise</span><span>to succeed with</span><span>your properties</span></p>
</main>
</body>
</html>
```